Web Site Design for a Finance (lending) Company

We are opening a new subsidiary that focuses on lending money in the real estate industry. We need a web site designed to represent the business.

The business is lending money to real estate investors. A typical client/borrower will be looking to borrow money to buy a house, renovate it and then sell it at a profit, all within 12 months or less.

Company name is Varlo Finance. Our logo is attached.

Attached is a general outline for the web site. We're working on writing more text for each page but this should give you enough to get started with some ideas.

Competitor web site that I like a lot (as an example): https://brixhallfunding.example/. Many of the general items on this site match what we will need (description of loan programs, FAQ)

Target Market(s)

Real estate investors (generally individuals or small companies with just a few people) who are buying homes, renovating them and then selling them at a profit.

Industry/Entity Type

Finance

Coding

Coded - Design and coding required

Number of Pages Required

5+ page

Colors

Designer to choose colors to be used in the design.

Requirements
Must have
• Minimalist design. Clean lines without too much clutter. Some stock photography is ok but the photos should not be distracting. They should almost fade in to the background so that user can focus on the key information about what our company does instead. We are a finance company, not a design company, so the information about our products will be more interesting to site visitors than the art.
• Some minimalist examples from Mosaiko:
• https://www.mosaiko.example/explore/minimalist-web-design/
Nice to have
• If you search in searchly for "hard money lenders" you will find many examples of web sites from our competition. I have provided a link above to competitor web site that I like a lot.
• I have attached our logo in EPS format. Logo is green. Web site doesn't have to be green but it should be of a color that will work well with the logo.

```html
<!DOCTYPE html>
<html lang="en">
<head>
<meta charset="utf-8">
<title>Varlo Finance – Contact Us</title>
<link rel="stylesheet" href="https://fonts.googleapis.com/css2?family=Lato:wght@300;400;700&family=Fira+Sans:wght@500&family=Roboto:wght@500;700&family=Montserrat:wght@600;700&display=swap">
<style>
:root{
  --green:#00522f;
  --green-dark:#003d24;
  --page:#f4f4f4;
  --ink:#3a3a3a;
  --muted:#666;
  --line:#d2d2d2;
  --white:#fff;
  --black:#1a1a1a;
}
*{box-sizing:border-box;margin:0;padding:0}
html,body{width:1200px;height:1031px;overflow:hidden}
body{position:relative;background:var(--page);font-family:'Lato',sans-serif;color:var(--ink)}
.abs{position:absolute}

.site-header{position:absolute;left:0;top:0;width:1200px;height:80px;background:var(--white)}
.brand{position:absolute;left:159px;top:22px;display:flex;align-items:center;gap:10px}
.brand-mark{width:30px;height:30px;background:var(--green)}
.brand-name{font-family:'Lato',sans-serif;font-weight:700;font-size:22px;color:var(--green)}
.call{position:absolute;left:799px;top:19px;display:flex;gap:7px}
.call-icon{width:42px;height:42px;background:var(--green);border-radius:6px;display:flex;align-items:center;justify-content:center}
.call-text{font-family:'Montserrat',sans-serif;line-height:1}
.call-title{font-size:26px;font-weight:700;color:var(--green);letter-spacing:.5px}
.call-number{font-size:16.5px;font-weight:600;color:var(--black);margin-top:2px}

.main-nav{position:absolute;left:0;top:80px;width:1200px;height:43px;background:var(--green)}
.main-nav a{position:absolute;top:14px;font-family:'Roboto',sans-serif;font-weight:700;font-size:14px;color:var(--white);text-decoration:none;letter-spacing:.2px}
.nav-social{position:absolute;top:9px;width:24px;height:24px;background:var(--white);border-radius:4px}

h1.section-title,h2.section-title{position:absolute;font-weight:400;font-size:32px;color:var(--ink);top:160px}
.intro{position:absolute;left:159px;top:208px;width:520px;font-weight:300;font-size:15px;line-height:24px;color:var(--muted)}
.field{position:absolute;background:var(--white);border:1px solid var(--line);font-size:12.5px;color:#8a8a8a;padding:0 10px;display:flex;align-items:center}
.field.note{align-items:flex-start;padding-top:16px}
.send{position:absolute;left:464px;top:567px;width:209px;height:43px;background:var(--green);color:var(--white);font-weight:700;font-size:16px;display:flex;align-items:center;justify-content:center}

.info-head{position:absolute;left:814px;font-family:'Fira Sans',sans-serif;font-weight:500;font-size:23px;color:var(--green)}
.info-icon{position:absolute;left:790px}
.info-text{position:absolute;left:814px;font-size:14px;line-height:16.5px;color:var(--muted)}

.site-footer{position:absolute;left:0;top:725px;width:1200px;height:306px;background:var(--green);color:var(--white)}
.foot-head{position:absolute;top:52px;font-size:28px;font-weight:400;letter-spacing:.3px}
.foot-link{position:absolute;font-size:17px;font-weight:400}
.signup-field{position:absolute;left:764px;top:110px;width:194px;height:42px;background:var(--white);color:#555;font-size:13px;padding-left:11px;display:flex;align-items:center;border-radius:2px 0 0 2px}
.signup-btn{position:absolute;left:958px;top:110px;width:111px;height:42px;background:var(--black);font-family:'Montserrat',sans-serif;font-weight:600;font-size:18px;display:flex;align-items:center;justify-content:center;border-radius:0 2px 2px 0}
.foot-social{position:absolute;top:173px;width:34px;height:34px;border:1.5px solid var(--white);border-radius:50%}
.foot-rule{position:absolute;left:0;top:244px;width:1200px;height:1px;background:rgba(255,255,255,.35)}
.copyright{position:absolute;left:126px;top:269px;font-family:'Montserrat',sans-serif;font-weight:600;font-size:13.5px}
.live-chat{position:absolute;left:749px;top:266px;width:320px;height:40px;background:var(--green-dark);font-family:'Montserrat',sans-serif;font-weight:600;font-size:14px;padding-left:12px;display:flex;align-items:center}
.chat-btn{position:absolute;top:12px;width:22px;height:18px;background:#0c5d39;border-radius:2px;display:flex;align-items:center;justify-content:center}
</style>
</head>
<body>

<header class="site-header">
  <div class="brand"><span class="brand-mark"></span><span class="brand-name">Varlo Finance</span></div>
  <div class="call">
    <div class="call-icon">
      <svg width="26" height="26" viewBox="0 0 24 24"><path fill="#fff" d="M6.6 10.8a15.1 15.1 0 0 0 6.6 6.6l2.2-2.2c.3-.3.7-.4 1-.2 1.1.4 2.3.6 3.6.6.6 0 1 .4 1 1V20c0 .6-.4 1-1 1A17 17 0 0 1 3 4c0-.6.4-1 1-1h3.5c.6 0 1 .4 1 1 0 1.3.2 2.5.6 3.6.1.3 0 .7-.2 1z"/></svg>
    </div>
    <div class="call-text">
      <div class="call-title">CALL US</div>
      <div class="call-number">555-014-LEND (5363)</div>
    </div>
  </div>
</header>

<nav class="main-nav">
  <a style="left:159px" href="#">HOME</a>
  <a style="left:233px" href="#">ABOUT US</a>
  <a style="left:332px" href="#">LOAN</a>
  <a style="left:398px" href="#">RESOURCES</a>
  <a style="left:502px" href="#">CONTACT US</a>
  <span class="nav-social" style="left:953px" aria-label="Social profile"></span>
  <span class="nav-social" style="left:985px" aria-label="Social profile"></span>
  <span class="nav-social" style="left:1016px" aria-label="Social profile"></span>
</nav>

<main>
  <h1 class="section-title" style="left:160px">Contact Us</h1>
  <p class="intro">Lorem ipsum dolor sit amet, consectetuer adipiscing elit, sed diam nonummy nibh euismod tincidunt ut laoreet dolore magna aliquam erat volutpat.</p>

  <div class="field" style="left:159px;top:283px;width:252px;height:44px">NAME</div>
  <div class="field" style="left:423px;top:283px;width:253px;height:44px">EMAIL</div>
  <div class="field" style="left:159px;top:354px;width:252px;height:44px">PHONE NUMBER</div>
  <div class="field" style="left:423px;top:354px;width:252px;height:44px">REFERRED BY (OPTIONAL)</div>
  <div class="field note" style="left:159px;top:424px;width:517px;height:128px">NOTE:</div>
  <div class="send">SEND</div>

  <h2 class="section-title" style="left:787px">Contact Info</h2>

  <svg class="info-icon" style="top:236px" width="16" height="22" viewBox="0 0 16 22"><path fill="#00522f" d="M8 0a8 8 0 0 0-8 8c0 6 8 14 8 14s8-8 8-14a8 8 0 0 0-8-8zm0 11a3 3 0 1 1 0-6 3 3 0 0 1 0 6z"/></svg>
  <div class="info-head" style="top:232px">Office Location</div>
  <div class="info-text" style="top:267px">4100 Harbor View Road, Suite<br>310 Bayside Point, CA 90000</div>

  <svg class="info-icon" style="top:320px;left:793px" width="11" height="18" viewBox="0 0 11 18"><rect x="1" y="1" width="9" height="16" rx="1.5" fill="none" stroke="#00522f" stroke-width="2"/><rect x="4" y="13" width="3" height="2" fill="#00522f"/></svg>
  <div class="info-head" style="top:315px">Phone:</div>
  <div class="info-text" style="top:350px">(555) 019-2740</div>

  <svg class="info-icon" style="top:393px" width="18" height="13" viewBox="0 0 18 13"><rect width="18" height="13" rx="1.5" fill="#00522f"/><path d="M1.5 2l7.5 5.5L16.5 2" fill="none" stroke="#f4f4f4" stroke-width="1.6"/></svg>
  <div class="info-head" style="top:384px">Email:</div>
  <div class="info-text" style="top:420px">info@varlofinance.example</div>
</main>

<footer class="site-footer">
  <h3 class="foot-head" style="left:124px">OUR INFO</h3>
  <h3 class="foot-head" style="left:303px">BOOKING</h3>
  <h3 class="foot-head" style="left:477px">ADDITIONAL LINKS</h3>
  <h3 class="foot-head" style="left:763px">STAY CONNECTED</h3>

  <span class="foot-link" style="left:126px;top:108px">HOMEPAGE</span>
  <span class="foot-link" style="left:126px;top:141px">ABOUT US</span>
  <span class="foot-link" style="left:126px;top:174px">HIRING</span>
  <span class="foot-link" style="left:305px;top:108px">BOOKING PAGE</span>
  <span class="foot-link" style="left:305px;top:141px">BLOG</span>
  <span class="foot-link" style="left:479px;top:108px">GIFT CARD</span>
  <span class="foot-link" style="left:479px;top:141px">HELP</span>
  <span class="foot-link" style="left:479px;top:174px">WE’RE GREEN</span>

  <div class="signup-field">EMAIL</div>
  <div class="signup-btn">SIGN UP</div>
  <span class="foot-social" style="left:763px" aria-label="Social profile"></span>
  <span class="foot-social" style="left:803px" aria-label="Social profile"></span>
  <span class="foot-social" style="left:844px" aria-label="Social profile"></span>
  <span class="foot-social" style="left:884px" aria-label="Social profile"></span>

  <div class="foot-rule"></div>
  <div class="copyright">Copyright Varlo @2017</div>
  <div class="live-chat">Live Chat
    <span class="chat-btn" style="left:259px"><svg width="12" height="12" viewBox="0 0 12 12"><circle cx="6" cy="6" r="6" fill="#fff"/><path d="M3.5 5l2.5 2.5L8.5 5" fill="none" stroke="#003d24" stroke-width="1.6"/></svg></span>
    <span class="chat-btn" style="left:285px"><svg width="11" height="11" viewBox="0 0 11 11"><path d="M5.5 1v9M1 5.5h9" stroke="#fff" stroke-width="2.2"/></svg></span>
  </div>
</footer>

</body>
</html>
```